business card deign

Logo needs the following on it.
1. attached logo
2. Tagline - "When the ice stays cold and the music plays...we made it!"
3. Name- Delia Fenwick, Founder and CPO
4. Address - 418 E. Harlow Avenue, Ste 2204, Tampa, FL. 33719
5. Phone - 720.555.0187

```html
<!DOCTYPE html>
<html lang="en">
<head>
<meta charset="utf-8">
<title>Tallowin Business Card</title>
<link href="https://fonts.googleapis.com/css2?family=Montserrat:ital,wght@0,400;0,500;0,700;1,400&display=swap" rel="stylesheet">
<style>
  :root {
    --backdrop: #333333;
    --card-light: #ffffff;
    --card-dark: #000000;
    --ink: #0d0d0d;
    --ink-soft: #6b6b6b;
    --paper-text: #ffffff;
  }
  * { box-sizing: border-box; margin: 0; padding: 0; }
  html, body {
    width: 1200px; height: 1145px; overflow: hidden;
    background: var(--backdrop);
    font-family: "Montserrat", Arial, sans-serif;
  }
  .stage {
    width: 1200px; height: 1145px;
    display: flex; align-items: center; justify-content: center; gap: 20px;
  }
  .card {
    position: relative;
    width: 560px; height: 320px;
    box-shadow: 0 6px 24px rgba(0,0,0,0.45);
  }
  .card--front { background: var(--card-light); color: var(--ink); }
  .card--back { background: var(--card-dark); color: var(--paper-text); }

  .brand {
    position: absolute;
    display: flex; flex-direction: column; align-items: center; gap: 12px;
  }
  .brand__dot { border-radius: 50%; background: currentColor; }
  .brand__name {
    font-weight: 700; letter-spacing: 0.32em; text-transform: uppercase;
    white-space: nowrap;
  }
  .card--front .brand { left: 92px; top: 118px; width: 130px; }
  .card--front .brand__dot { width: 34px; height: 34px; }
  .card--front .brand__name { font-size: 15px; }
  .card--back .brand { left: 0; right: 0; top: 102px; }
  .card--back .brand__dot { width: 46px; height: 46px; }
  .card--back .brand__name { font-size: 20px; }

  .contact { position: absolute; left: 298px; top: 104px; }
  .contact__name { font-size: 26px; font-weight: 700; line-height: 1; letter-spacing: -0.01em; }
  .contact__role { font-size: 10px; font-style: italic; color: var(--ink-soft); margin-top: 5px; }
  .contact__rule { width: 28px; height: 3px; background: var(--ink); border-radius: 2px; margin: 9px 0 14px; }
  .contact__row { display: flex; align-items: flex-start; gap: 10px; font-size: 11px; color: var(--ink-soft); line-height: 1.3; margin-bottom: 10px; }
  .contact__icon { width: 12px; height: 13px; flex: none; margin-top: 1px; fill: var(--ink); }

  .tagline {
    position: absolute; left: 0; right: 0; top: 276px;
    text-align: center; font-size: 11px; font-weight: 500;
  }
</style>
</head>
<body>
<main class="stage">
  <section class="card card--front">
    <div class="brand">
      <span class="brand__dot"></span>
      <span class="brand__name">Tallowin</span>
    </div>
    <div class="contact">
      <h1 class="contact__name">Delia Fenwick</h1>
      <p class="contact__role">Founder and CPO</p>
      <div class="contact__rule"></div>
      <p class="contact__row">
        <svg class="contact__icon" viewBox="0 0 24 24" aria-hidden="true"><path d="M6.6 10.8a15.1 15.1 0 0 0 6.6 6.6l2.2-2.2a1 1 0 0 1 1-.25 11.4 11.4 0 0 0 3.6.57 1 1 0 0 1 1 1V20a1 1 0 0 1-1 1A17 17 0 0 1 3 4a1 1 0 0 1 1-1h3.5a1 1 0 0 1 1 1c0 1.25.2 2.45.57 3.57a1 1 0 0 1-.25 1z"/></svg>
        <span>+1 (720) 555 0187</span>
      </p>
      <p class="contact__row">
        <svg class="contact__icon" viewBox="0 0 24 24" aria-hidden="true"><path d="M12 2a7 7 0 0 0-7 7c0 5.2 7 13 7 13s7-7.8 7-13a7 7 0 0 0-7-7zm0 9.5A2.5 2.5 0 1 1 12 6.5a2.5 2.5 0 0 1 0 5z"/></svg>
        <span>418 E. Harlow Avenue,<br>Ste 2204, Tampa, FL. 33719</span>
      </p>
    </div>
  </section>

  <section class="card card--back">
    <div class="brand">
      <span class="brand__dot"></span>
      <span class="brand__name">Tallowin</span>
    </div>
    <p class="tagline">When the ice stays cold and the music plays...we made it!</p>
  </section>
</main>
</body>
</html>
```